Web Header needed for an inspirational coaching company's website - ongoing work

We need a beautifully designed web header to replace my current one at my homepage on my website www.brekavol.com
There will be continuous work required for various creative work in the future if your work is selected.
I work with corporate professionals and executives to bring clarity and joy back to their career. It needs to be elegant, sophisticated, intelligent, but friendly and inspiring at the same time.
Brief and the sample header size are attached in my files
Thank you!
Target Market(s)
Corporate profesionals and executives
Industry/Entity Type
It Company
Colors
Designer to choose colors to be used in the design.
Look and feel
Each slider illustrates characteristics of the customer's brand and the style your logo design should communicate.

```html
<!DOCTYPE html>
<html lang="en">
<head>
<meta charset="utf-8">
<title>Clearpath — Your Career Partner</title>
<link rel="stylesheet" href="https://fonts.googleapis.com/css2?family=Oswald:wght@700&family=Roboto:wght@300&family=Source+Sans+3:wght@600&display=swap">
<style>
  :root {
    --page: #ffffff;
    --slate: #58585a;
    --slate-light: #626264;
    --orange: #e27037;
    --white: #ffffff;
    --ink: #2f2f2f;
  }
  html, body {
    margin: 0;
    padding: 0;
    width: 1200px;
    height: 1200px;
    overflow: hidden;
    background: var(--page);
  }
  .header-banner {
    position: absolute;
    left: 89px;
    top: 387px;
    width: 1025px;
    height: 463px;
    overflow: hidden;
    background: var(--orange);
  }
  .header-banner__backdrop {
    position: absolute;
    left: 0;
    top: 0;
    width: 100%;
    height: 265px;
    background: linear-gradient(90deg, var(--slate) 0%, var(--slate-light) 50%, var(--slate) 100%);
  }
  .brand {
    position: absolute;
    left: 50px;
    top: 40px;
    display: flex;
    align-items: center;
    gap: 10px;
    font-family: "Roboto", Arial, sans-serif;
    font-weight: 300;
    font-size: 30px;
    letter-spacing: 3px;
    color: var(--white);
  }
  .brand__dot {
    width: 12px;
    height: 12px;
    border-radius: 50%;
    background: var(--orange);
  }
  .headline {
    position: absolute;
    left: 117px;
    top: 132px;
    margin: 0;
    font-family: "Oswald", "Arial Narrow", sans-serif;
    font-weight: 700;
    font-size: 138px;
    line-height: 1;
    color: var(--white);
  }
  .subhead {
    position: absolute;
    left: 125px;
    top: 274px;
    margin: 0;
    font-family: "Roboto", Arial, sans-serif;
    font-weight: 300;
    font-size: 64px;
    line-height: 1;
    color: var(--white);
    letter-spacing: -0.5px;
  }
  .tagline {
    position: absolute;
    left: 131px;
    top: 350px;
    width: 377px;
    height: 39px;
    background: var(--white);
    display: flex;
    align-items: center;
    justify-content: center;
    font-family: "Source Sans 3", Arial, sans-serif;
    font-weight: 600;
    font-size: 25px;
    color: var(--ink);
  }
  .coach-portrait {
    position: absolute;
    left: 680px;
    top: 0;
    width: 345px;
    height: 463px;
    background: linear-gradient(180deg, #2a2624 0%, #c9a08c 40%, #3a2f2b 62%, #e4753c 100%);
  }
</style>
</head>
<body>
  <section class="header-banner">
    <div class="header-banner__backdrop"></div>
    <div class="brand"><span class="brand__name">CLEARPATH</span><span class="brand__dot"></span></div>
    <h1 class="headline">Your</h1>
    <p class="subhead">CAREER PARTNER</p>
    <div class="tagline">Bring Clarity to Your Career</div>
    <div class="coach-portrait" role="img" aria-label="Portrait photo of the smiling career coach with long dark hair in an orange top"></div>
  </section>
</body>
</html>
```